Morrow Engineering Core Values Branding Package

Morrow Engineering has recently refined its company Core Values and is seeking a strong, cohesive branding package to visually bring these values to life. The new graphic assets will communicate our commitment to excellence in a way that resonates with our team, clients, and partners in a blue-collar, industrial environment.

We are looking for multiple visual assets with consistent design elements that can be applied across platforms. The tone should reflect strength, reliability, and professionalism while remaining approachable and aligned with our industry.

Core Values & Descriptions
Accountability
“We take ownership of our work and actions, ensuring reliability and trust in every solution we deliver.”

Teamwork
“We collaborate across departments and disciplines to provide the highest level of service and innovation for our clients.”

Integrity
“We operate with honesty, transparency, and ethical standards in all aspects of our business.”

Growth
“We are committed to continuous improvement—of our people, our processes, and our impact in the industry.”

Deliverables

1. Primary Core Values Graphic
A master visual representing all four values together.
Designed for use on posters, office signage, internal presentations.

2. Individual Value Graphics (x4)
One graphic per core value: Accountability, Teamwork, Integrity, Growth.
Cohesive style with slight visual variation to reflect each value’s unique meaning.

Target Market(s)

Employees of Morrow Engineering

Industry/Entity Type

Blue Collar

Font styles to use
Sans Serif

Colors
0054AA
0677BA
7BADD7
CADEEF
E8F1F8
00AB8E
00BBA5
67D7C9
C6EFE9
E9F9F6
EB3D1F
EC4F4E
F09395
F8D3D4
FCEDEE

Requirements
Must have
• Accountability, Teamwork, Integrity, Growth

```html
<!DOCTYPE html>
<html lang="en">
<head>
<meta charset="utf-8">
<title>Morrow Engineering – Core Values</title>
<link rel="stylesheet" href="https://fonts.googleapis.com/css2?family=Roboto+Condensed:wght@300;400;700&display=swap">
<style>
  :root {
    --navy: #00315f;
    --green: #3bab2b;
    --red: #c8102e;
    --white: #ffffff;
    --tint: #eef7ec;
    --mist: #eeeff4;
    --page: #f2f2f2;
    --rule: #8da2bd;
  }
  html, body {
    margin: 0;
    width: 1200px;
    height: 1146px;
    overflow: hidden;
    background: var(--page);
    font-family: "Roboto Condensed", Arial, sans-serif;
  }
  .poster {
    position: absolute;
    left: 0;
    top: 150px;
    width: 1200px;
    height: 845px;
    overflow: hidden;
    background: var(--white);
  }
  .poster-art {
    position: absolute;
    inset: 0;
  }
  .brand-name {
    position: absolute;
    top: 86px;
    left: 0;
    width: 1200px;
    margin: 0;
    text-align: center;
    color: var(--navy);
    font-weight: 700;
    font-size: 56px;
    letter-spacing: 1px;
    text-transform: uppercase;
    line-height: 1;
  }
  .value {
    position: absolute;
    top: 606px;
    width: 250px;
    text-align: center;
    color: var(--white);
  }
  .value-title {
    margin: 0;
    font-weight: 700;
    font-size: 31px;
    line-height: 40px;
    letter-spacing: 0.2px;
  }
  .value-rule {
    width: 132px;
    height: 1px;
    margin: 5px auto 8px;
    background: var(--rule);
  }
  .value-text {
    margin: 0 auto;
    width: 200px;
    font-weight: 300;
    font-size: 15.5px;
    line-height: 20px;
  }
  .value--accountability { left: 85px; }
  .value--teamwork { left: 346px; }
  .value--integrity { left: 608px; }
  .value--growth { left: 868px; }
  .website {
    position: absolute;
    top: 798px;
    left: 0;
    width: 1200px;
    display: flex;
    justify-content: center;
    align-items: center;
    gap: 12px;
    color: var(--white);
    font-size: 28px;
    font-weight: 400;
    line-height: 1;
  }
</style>
</head>
<body>
<main class="poster">
  <svg class="poster-art" viewBox="0 0 1200 845" width="1200" height="845" aria-hidden="true">
    <defs>
      <filter id="soft-shadow" x="-30%" y="-30%" width="160%" height="160%">
        <feDropShadow dx="0" dy="4" stdDeviation="6" flood-color="#000" flood-opacity="0.18"/>
      </filter>
      <linearGradient id="band-left" x1="0" x2="1" y1="0" y2="0">
        <stop offset="0" stop-color="#3bab2b"/>
        <stop offset="0.55" stop-color="#3bab2b"/>
        <stop offset="1" stop-color="#00315f"/>
      </linearGradient>
      <linearGradient id="band-right" x1="1" x2="0" y1="0" y2="0">
        <stop offset="0" stop-color="#3bab2b"/>
        <stop offset="0.65" stop-color="#3bab2b"/>
        <stop offset="1" stop-color="#00315f"/>
      </linearGradient>
      <g id="value-badge">
        <polygon points="-33,47 -33,18 0,0 33,18 33,47" fill="var(--navy)"/>
        <polygon points="0,29 106,84 106,204 0,260 -106,204 -106,84" fill="var(--white)" filter="url(#soft-shadow)"/>
        <polygon points="0,44 91,91 91,197 0,246 -91,197 -91,91" fill="var(--red)"/>
        <polygon points="0,45 72,84 72,281 0,314 -72,281 -72,84" fill="var(--green)" filter="url(#soft-shadow)"/>
        <polygon points="0,85 56,117 56,182 0,214 -56,182 -56,117" fill="var(--white)"/>
        <circle cx="0" cy="321" r="26" fill="var(--white)" filter="url(#soft-shadow)"/>
        <circle cx="0" cy="321" r="13" fill="var(--green)"/>
        <line x1="0" y1="346" x2="0" y2="372" stroke="var(--green)" stroke-width="4"/>
        <polygon points="-12,368 12,368 0,380" fill="var(--green)"/>
      </g>
    </defs>

    <!-- backdrop sweeps -->
    <rect width="1200" height="845" fill="var(--tint)"/>
    <path d="M0,225 C300,80 700,10 1000,60 C1120,85 1200,200 1200,300 L1200,845 L0,845 Z" fill="var(--white)"/>
    <path d="M0,340 C300,220 620,170 860,200 C1000,220 1080,300 1100,420 L1200,420 L1200,845 L0,845 Z" fill="var(--mist)"/>
    <path d="M0,390 C300,280 600,250 820,270 C960,285 1020,340 1040,420 L1200,460 L1200,845 L0,845 Z" fill="var(--white)"/>

    <!-- navy field with red rule -->
    <path d="M0,466 L1200,466 L1200,845 L0,845 Z" fill="var(--navy)"/>
    <polyline points="0,453 110,453 140,470 M0,0" fill="none" stroke="var(--red)" stroke-width="2"/>
    <polyline points="0,453 110,453 135,466" fill="none" stroke="var(--red)" stroke-width="2"/>
    <polyline points="280,466 310,455 370,455 398,466" fill="none" stroke="var(--red)" stroke-width="2"/>
    <polyline points="542,466 572,455 632,455 660,466" fill="none" stroke="var(--red)" stroke-width="2"/>
    <polyline points="804,466 834,455 894,455 922,466" fill="none" stroke="var(--red)" stroke-width="2"/>
    <polyline points="1064,466 1094,453 1200,453" fill="none" stroke="var(--red)" stroke-width="2"/>

    <!-- bottom bands -->
    <rect x="0" y="791" width="313" height="54" fill="url(#band-left)"/>
    <rect x="887" y="791" width="313" height="54" fill="url(#band-right)"/>

    <!-- badges -->
    <use href="#value-badge" x="210" y="214"/>
    <use href="#value-badge" x="471" y="214"/>
    <use href="#value-badge" x="733" y="214"/>
    <use href="#value-badge" x="993" y="214"/>

    <!-- icons -->
    <g fill="none" stroke="var(--navy)" stroke-width="2.2" stroke-linecap="round" stroke-linejoin="round">
      <g class="icon-accountability" transform="translate(210,363)">
        <path d="M6,-30 L24,-24 V-10 C24,2 16,9 6,13 C-4,9 -12,2 -12,-10 V-24 Z"/>
        <path d="M-2,-12 L4,-6 L15,-18"/>
        <path d="M-28,18 L-18,12 H-4 C2,12 2,19 -4,19 H-12 M-4,19 H10 L26,10"/>
        <path d="M-30,22 L-22,32 M-22,32 H8 L26,18"/>
      </g>
      <g class="icon-teamwork" transform="translate(471,363)">
        <rect x="-22" y="-4" width="20" height="20" rx="2" transform="rotate(-35 -12 6)"/>
        <rect x="2" y="-20" width="20" height="20" rx="2" transform="rotate(-35 12 -10)"/>
        <circle cx="0" cy="-2" r="4"/>
        <path d="M-34,24 L-24,14 M24,-22 L34,-32"/>
      </g>
      <g class="icon-integrity" transform="translate(733,363)">
        <path d="M0,-32 L10,-28 V-20 C10,-14 5,-11 0,-9 C-5,-11 -10,-14 -10,-20 V-28 Z"/>
        <path d="M-4,-21 L-1,-18 L5,-24"/>
        <rect x="-34" y="-10" width="10" height="26" rx="2" transform="rotate(-15 -29 3)"/>
        <rect x="24" y="-10" width="10" height="26" rx="2" transform="rotate(15 29 3)"/>
        <path d="M-24,-4 L-10,-8 L4,-2 L22,-6 M-24,12 L-6,24 C-2,26 2,24 4,20 L22,8"/>
        <path d="M-8,4 L6,14 M-2,0 L12,10"/>
      </g>
      <g class="icon-growth" transform="translate(993,363)">
        <rect x="-24" y="4" width="9" height="18"/>
        <rect x="-8" y="-6" width="9" height="28"/>
        <rect x="8" y="-16" width="9" height="38"/>
        <path d="M-32,22 H30"/>
        <path d="M-30,-8 C-10,-10 10,-18 24,-30"/>
        <path d="M16,-31 L24,-30 L22,-22"/>
      </g>
    </g>
  </svg>

  <h1 class="brand-name">Morrow Engineering</h1>

  <section class="value value--accountability">
    <h2 class="value-title">ACCOUNTABILITY</h2>
    <div class="value-rule"></div>
    <p class="value-text">We take ownership of our work and actions, ensuring reliability and trust in every solution we deliver.</p>
  </section>
  <section class="value value--teamwork">
    <h2 class="value-title">TEAMWORK</h2>
    <div class="value-rule"></div>
    <p class="value-text">We collaborate across departments and disciplines to provide the highest level of service and innovation for our clients.</p>
  </section>
  <section class="value value--integrity">
    <h2 class="value-title">INTEGRITY</h2>
    <div class="value-rule"></div>
    <p class="value-text">We operate with honesty, transparency, and ethical standards in all aspects of our business.</p>
  </section>
  <section class="value value--growth">
    <h2 class="value-title">GROWTH</h2>
    <div class="value-rule"></div>
    <p class="value-text">We are committed to continuous improvement—of our people, our processes, and our impact in the industry.</p>
  </section>

  <div class="website">
    <svg width="20" height="20" viewBox="0 0 20 20" aria-hidden="true" fill="none" stroke="#3bab2b" stroke-width="1.6">
      <circle cx="10" cy="10" r="8.5"/>
      <ellipse cx="10" cy="10" rx="3.8" ry="8.5"/>
      <path d="M1.5,10 H18.5 M3,5.5 H17 M3,14.5 H17"/>
    </svg>
    <span>www.morroweng.com</span>
  </div>
</main>
</body>
</html>
```